Pagina Lartécnica

The Lartécnica is a company dealing with leasing and selling real estate. The current site can be accessed at www.lartecnica-exemplo.com.br. We intend to redesign the look of the site and for that we would like to redesign the home page and the page with information and pictures of the property. The homepage should maintain the characteristics of the current common design simple, short and straightforward. The page with the data of the properties should be accessed with two changes page as it is currently running. The search from the map by region and should be maintained.
The page containing the information of the property will provide a total of 15 small pictures that when clicked will appear in larger size. The colors to be used should be orange, blue, black and white. The map can be maintained in the current colors.
Updates

Project Deadline Extended
Reason: Payment guarante!!

Payment guaranteed. Deadline for submission of designs April 27.

Industry/Entity Type

Real Estate

Requirements
Must have
• Search by map regions and search box
address
keep colors from the current page
phones
clean look
Nice to have
• clean look
Should not have
• We like the current page. We just want to make it compatible with modern and new design trends and monitors.

```html
<!DOCTYPE html>
<html lang="en">
<head>
<meta charset="utf-8">
<title>Lartécnica</title>
<link href="https://fonts.googleapis.com/css2?family=Montserrat:wght@700&family=Cabin:wght@400;500;600&family=Signika:wght@300&family=Arimo:wght@400;700&display=swap" rel="stylesheet">
<style>
:root{
  --orange:#f47a0c;
  --orange-dark:#e86a00;
  --orange-light:#ff9a1f;
  --navy:#2a2a78;
  --navy-text:#3a3552;
  --brown:rgba(90,40,0,.78);
  --white:#ffffff;
  --line:#e6e6e6;
  --footer-bg:#f5f5f5;
  --footer-text:#555555;
  --muted:#777777;
}
*{margin:0;padding:0;box-sizing:border-box}
html,body{width:1200px;height:742px;overflow:hidden;background:var(--white)}
body{position:relative;font-family:"Cabin",sans-serif}
.top-band{position:absolute;left:0;top:0;width:1200px;height:172px;
  background:linear-gradient(100deg,#f07a08 0%,#fb8e1a 35%,#f37d0c 60%,#fa8c1b 100%)}
.main-nav{position:absolute;top:36px;left:138px;display:flex;gap:31px}
.main-nav a{font-family:"Montserrat",sans-serif;font-weight:700;font-size:14px;color:var(--white);text-decoration:none;letter-spacing:.2px;text-shadow:0 1px 1px rgba(0,0,0,.2)}
.phones{position:absolute;left:737px;top:23px;width:339px;height:43px;background:var(--brown);border-radius:3px;
  color:var(--white);font-family:"Arimo",sans-serif;font-size:14px;display:flex;align-items:center;justify-content:center;gap:6px}
.phones b{font-family:"Montserrat",sans-serif;font-size:14px}
.brand{position:absolute;left:121px;top:89px;width:261px;height:120px;background:var(--white);
  box-shadow:0 6px 8px -4px rgba(0,0,0,.25);display:flex;align-items:center;justify-content:center;gap:10px}
.brand-mark{width:22px;height:22px;background:var(--navy)}
.brand-name{font-family:"Cabin",sans-serif;font-weight:600;font-size:36px;color:var(--navy)}
.side-menu{position:absolute;left:122px;top:226px;width:258px;list-style:none}
.side-menu li{height:36px;border-bottom:1px solid var(--line);padding-left:22px;line-height:36px;font-size:15px;font-weight:500;color:var(--navy-text)}
.side-menu li:last-child{border-bottom:none}
.search-box{position:absolute;left:121px;top:385px;width:260px;height:163px;border:1px solid var(--line);border-radius:3px;background:var(--white)}
.search-title{height:37px;background:linear-gradient(var(--orange-light),var(--orange-dark));color:var(--white);font-size:16px;font-weight:500;line-height:37px;padding-left:25px;border-radius:3px 3px 0 0}
.deal-type{display:flex;justify-content:center;align-items:center;margin-top:15px;font-size:15px;font-weight:500;color:var(--navy-text)}
.deal-type span{display:flex;align-items:center;gap:8px;padding:0 14px}
.deal-type .divider{width:1px;height:26px;background:var(--line);padding:0}
.radio{width:16px;height:16px;border-radius:50%;border:1px solid #c8c8c8;background:linear-gradient(#fff,#e6e6e6);position:relative}
.radio.on::after{content:"";position:absolute;left:4px;top:4px;width:6px;height:6px;border-radius:50%;background:#555}
.select{position:absolute;left:29px;top:90px;width:197px;height:33px;border:1px solid var(--line);border-radius:3px;background:linear-gradient(#fff,#f3f3f3);
  font-family:"Arimo",sans-serif;font-size:13px;color:#444;line-height:31px;padding-left:12px}
.select::after{content:"";position:absolute;right:11px;top:13px;border-left:5px solid transparent;border-right:5px solid transparent;border-top:6px solid #888}
.search-btn{position:absolute;left:152px;top:523px;width:196px;height:42px;background:var(--white);border:1px solid var(--line);border-radius:3px;
  display:flex;align-items:center;justify-content:center;gap:4px;font-size:20px;font-weight:600;color:var(--orange)}
.region-panel{position:absolute;left:417px;top:89px;width:660px;height:473px;border-radius:3px;overflow:hidden;
  background:linear-gradient(180deg,#ffffff 0%,#f7f7f7 100%);box-shadow:0 1px 4px rgba(0,0,0,.25)}
.region-map{position:absolute;left:0;top:0;width:335px;height:473px;background:linear-gradient(180deg,#363a8e 0%,#2b2d78 100%)}
.region-name{position:absolute;left:361px;top:120px;font-family:"Signika",sans-serif;font-weight:300;font-size:52px;line-height:1;color:var(--orange)}
.districts{position:absolute;top:186px;list-style:none;font-size:14px;line-height:22px;color:#111}
.districts.col-a{left:364px}
.districts.col-b{left:497px}
.panel-note{position:absolute;left:0;bottom:0;width:660px;height:52px;background:linear-gradient(90deg,rgba(230,230,230,0) 40%,#ececec 100%);
  text-align:right;padding-right:24px;line-height:52px;font-size:14px;color:#111}
.site-footer{position:absolute;left:0;top:627px;width:1200px;height:115px;background:var(--footer-bg);border-top:1px solid #e8e8e8;text-align:center;font-family:"Arimo",sans-serif}
.address{margin-top:29px;font-size:13px;font-weight:700;color:var(--footer-text)}
.address span{font-weight:400}
.copyright{margin-top:25px;font-size:12px;color:var(--muted)}
</style>
</head>
<body>
<header class="top-band">
  <nav class="main-nav">
    <a href="#">COMPANY</a><a href="#">LOCATION</a><a href="#">RESTRICTED AREA</a><a href="#">CONTACT US</a>
  </nav>
  <div class="phones"><b>LEASE</b> (48) 3100-2040 &nbsp;|&nbsp; <b>SALES</b> (48) 9100-5060</div>
</header>

<div class="brand"><span class="brand-mark"></span><span class="brand-name">Lartécnica</span></div>

<ul class="side-menu">
  <li>List your Property</li>
  <li>Information to Owner</li>
  <li>Information for the Tenant</li>
  <li>Request your Property</li>
</ul>

<form class="search-box">
  <div class="search-title">Search for Properties</div>
  <div class="deal-type">
    <span>To Buy <i class="radio"></i></span>
    <span class="divider"></span>
    <span>To Rent <i class="radio on"></i></span>
  </div>
  <div class="select">All Properties</div>
</form>
<div class="search-btn">Buscar
  <svg width="22" height="22" viewBox="0 0 22 22"><circle cx="9" cy="9" r="6.5" fill="none" stroke="#f47a0c" stroke-width="3"/><line x1="14" y1="14" x2="20" y2="20" stroke="#f47a0c" stroke-width="3.5" stroke-linecap="round"/></svg>
</div>

<section class="region-panel">
  <div class="region-map" role="img" aria-label="Map of the island regions with the Norte region highlighted in orange"></div>
  <h2 class="region-name">Norte</h2>
  <ul class="districts col-a">
    <li>Daniela</li><li>Cachoeira</li><li>Cacupe</li><li>Canasvieiras</li><li>Ingleses Joao Paulo</li><li>Jurere</li><li>Monte Verde</li><li>Ponta Das Canas</li>
  </ul>
  <ul class="districts col-b">
    <li>Ratones</li><li>Rio Vermelho</li><li>Saco Grande</li><li>Sto. Antonio</li><li>Vargem do Born Jesus</li><li>Grande</li><li>Pequena</li>
  </ul>
  <p class="panel-note">A Lartécnica nao efetua alugueis para temporada</p>
</section>

<footer class="site-footer">
  <p class="address">Rua das Palmeiras, 140 - Corner with Antonio Lima Street - Downtown - Florianópolis &nbsp; CEP: <span>88000-100</span> - Fax: (48) <span>3100-2041</span></p>
  <p class="copyright">© 2013 - Lartécnica - All Rights Reserved.</p>
</footer>
</body>
</html>
```